Bref créative
Business Cards for a Start-Up
Wholesaler of Construction Products
Professional
Marva Quintero
President
472 West Palmera Ln., Ste C204
Hagatna, GU 96842
marva@pacificbedrockco.com
www.pacificbedrockco.com
Reefstone Supply, Inc. is a start-up company that will be wholesaling construction products (e.g., concrete, asphalt, etc.) to prime construction contractors. The business cards should be straight-forward and easy to read. We are colored backgrounds. If you have any questions, please post in the project discussion area.

```html
<!DOCTYPE html>
<html lang="en">
<head>
<meta charset="utf-8">
<title>Reefstone Supply, Inc. — Stationery</title>
<link rel="stylesheet" href="https://fonts.googleapis.com/css2?family=Arimo:wght@400;700&display=swap">
<style>
  :root {
    --paper: #ffffff;
    --edge: #9a9a9a;
    --ink: #555555;
    --ink-dark: #3f3f3f;
    --band: #8a8a8a;
    --band-dark: #6e6e6e;
    --band-light: #c4c4c4;
    --on-band: #ffffff;
  }
  * { box-sizing: border-box; margin: 0; padding: 0; }
  html, body { width: 1200px; height: 845px; overflow: hidden; background: var(--paper); }
  body { position: relative; font-family: "Arimo", Arial, sans-serif; color: var(--ink); }

  .sheet { position: absolute; background: var(--paper); border: 1px solid var(--edge); overflow: hidden; }

  .brand { position: absolute; display: flex; align-items: flex-start; gap: 8px; }
  .brand-mark { width: 34px; height: 34px; background: var(--band-dark); flex: none; }
  .brand-name { font-weight: 700; font-size: 20px; line-height: 1; color: var(--band-dark); text-transform: uppercase; }
  .brand-tag { font-size: 8px; letter-spacing: .5px; text-transform: uppercase; color: var(--ink); margin-top: 5px; font-weight: 400; }

  .address { position: absolute; font-size: 11px; line-height: 1.45; color: var(--ink); }

  /* Letterhead */
  .letterhead { left: 67px; top: 34px; width: 581px; height: 758px; }
  .letterhead .brand { left: 28px; top: 20px; }
  .letterhead .address { left: 28px; top: 98px; }
  .letterhead .contact-line { position: absolute; left: 28px; top: 690px; font-size: 11px; display: flex; gap: 58px; }
  .letterhead .foot-band { position: absolute; left: 0; right: 0; bottom: 0; height: 42px; background: var(--band); border-top: 4px solid var(--band-light); color: var(--on-band); font-size: 11px; display: flex; align-items: center; gap: 70px; padding-left: 28px; }

  /* Envelope */
  .envelope { left: 192px; top: 276px; width: 948px; height: 396px; }
  .envelope .brand { left: 30px; top: 36px; }
  .envelope .address { left: 30px; top: 322px; }
  .envelope .foot-band { position: absolute; left: 0; right: 0; bottom: 8px; height: 34px; background: var(--band); border-top: 4px solid var(--band-light); color: var(--on-band); font-size: 11px; display: flex; align-items: center; gap: 60px; padding-left: 30px; }
  .envelope .foot-rule { position: absolute; left: 0; right: 0; bottom: 0; height: 4px; background: var(--band-light); }

  /* Business card */
  .card { left: 665px; top: 34px; width: 475px; height: 278px; }
  .card .backdrop { position: absolute; inset: 0; }
  .card .brand { left: 20px; top: 56px; width: 190px; }
  .card .brand-mark { width: 30px; height: 30px; }
  .card .brand-name { font-size: 16px; line-height: 1.1; }
  .card .brand-tag { font-size: 6px; letter-spacing: .2px; margin-top: 4px; }
  .card .holder { position: absolute; left: 258px; top: 40px; color: var(--on-band); }
  .card .holder-name { font-size: 22px; font-weight: 700; }
  .card .holder-title { font-size: 17px; margin-top: 4px; }
  .card .card-address { position: absolute; right: 16px; top: 140px; text-align: right; color: var(--on-band); font-size: 11px; line-height: 1.4; }
  .card .card-web { position: absolute; right: 16px; top: 222px; text-align: right; color: var(--on-band); font-size: 11px; line-height: 1.5; }
  .label { margin-right: 6px; }
</style>
</head>
<body>

  <section class="sheet letterhead">
    <div class="brand">
      <span class="brand-mark"></span>
      <div><div class="brand-name">Reefstone Supply, Inc.</div><div class="brand-tag">Wholesaler of Construction Materials</div></div>
    </div>
    <p class="address">472 West Palmera Ln., Ste C204<br>Hagatna, GU 96842</p>
    <p class="contact-line"><span><span class="label">Phone</span>(671) 555-0142</span><span><span class="label">Fax</span>(671) 555-0187</span></p>
    <div class="foot-band"><span><span class="label">Email</span>marva@pacificbedrockco.com</span><span><span class="label">Web</span>www.pacificbedrockco.com</span></div>
  </section>

  <section class="sheet envelope">
    <div class="brand">
      <span class="brand-mark"></span>
      <div><div class="brand-name">Reefstone Supply, Inc.</div><div class="brand-tag">Wholesaler of Construction Materials</div></div>
    </div>
    <p class="address">472 West Palmera Ln., Ste C204, Hagatna, GU 96842</p>
    <div class="foot-band">
      <span><span class="label">Phone</span>(671) 555-0142</span>
      <span><span class="label">Fax</span>(671) 555-0187</span>
      <span><span class="label">Email</span>marva@pacificbedrockco.com</span>
      <span><span class="label">Web</span>www.pacificbedrockco.com</span>
    </div>
    <div class="foot-rule"></div>
  </section>

  <section class="sheet card">
    <svg class="backdrop" width="475" height="278" viewBox="0 0 475 278" aria-hidden="true">
      <path d="M236 278 L236 70 Q236 0 306 0 L475 0 L475 278 Z" fill="var(--band)"/>
      <path d="M226 278 L226 70 Q226 -10 306 -10" fill="none" stroke="var(--band-light)" stroke-width="4"/>
    </svg>
    <div class="brand">
      <span class="brand-mark"></span>
      <div><div class="brand-name">Reefstone<br>Supply, Inc.</div><div class="brand-tag">Wholesaler of Construction Materials</div></div>
    </div>
    <div class="holder">
      <div class="holder-name">Marva Quintero</div>
      <div class="holder-title">President</div>
    </div>
    <p class="card-address">472 West Palmera Ln., Ste C204<br>Hagatna, GU 96842<br><span class="label">Phone</span>(671) 555-0142<br><span class="label">Fax</span>(671) 555-0187</p>
    <p class="card-web"><span class="label">Email</span>marva@pacificbedrockco.com<br><span class="label">Web</span>www.pacificbedrockco.com</p>
  </section>

</body>
</html>
```